Smart, intuitive SaaS software dashboard design

PactBloom is an innovative modern SaaS (software as a service) solution for contract and meeting management.

What we are looking for is fresh ideas for our dashboard. We do not need web coding or actionable wireframes now – but purely great design ideas from where to continue forward.

How should a modern web software dashboard look like? Fresh, intuitive, easy-to-use, and adaptable for responsive mobile designs. We hope that when the user logs into the service and sees the dashboard, he/she gets a good big picture of the current status of the most important documents of his/hers company.

To get to know the service and see the components, we kindly ask you to register to our service at www.pactbloom-demo.net and to utilize the free trial (30 days) so you can see the existing dashboard live. And also try out how it works. Might help you to get ideas how to improve it.

(The designer we will choose might be offered later on to design some other pages as well (contract view and edit pages, meeting page etc).)

You’ll find additional information in the attachment.

You’ll find more information of the company and the service also at www.pactbloom-demo.net

Target Market(s)

Global

Industry/Entity Type

Business Management

Number of Pages Required

1 page

Font styles to use
Sans Serif

Requirements
Must have
• 1) Clear design idea for us to iterate from, 2) Modern look and feel - elegant & bold at the same time - still with credibility in our target group. And 3) Suitable for dashboard usage - it should it a clear big picture for the user.
• UPDATE:
• Users should see most important things with one glance. Therefore we would like to see AT LEAST these items mentioned below on the first page.
• NOTE: if all these things are visible on the dashboard, the menu list is maybe not needed on the left. (And there might be some icons on the top header with needed settings/inbox features anyway.)
• NOTE2: as explained earlier, the design should be responsive i.e. work without modifications in PC, iPad and mobile (the areas/boxes would just rearrange themselves on top of each other.)
• -First area should be Documents, which would include different document categories: Contracts, Finance & Admin and HR
• -All different types of Meetings could be the next area (upcoming ones clearly visible with date and maybe description, time and location visible also).
• -Reminders and Activity Feed (they might also be together in top of each other, so that Reminder is visible first and Activity feed can be chosen from the tab.)
• -Virtual Datarooms (maybe 1-3 different ones with some analytics for each visible e.g. like usage/visits per day)
• Saved searches in very important list as users can save their most important searches. There are typically many of these, so at least 5 should be visible and then see all button (maybe even more could be visible if they fit on your design)
• My Latest is also important.
• (As explained, Action Required area is NOT needed anymore).
Nice to have
• Surprise us!
Should not have
• Please avoid the boring traditional legacy stuff and the common report dashboards.
• You do not need design a 100% mockup for the techie to continue with. The ideas count.

```html
<!DOCTYPE html>
<html lang="en">
<head>
<meta charset="utf-8">
<title>PactBloom Dashboard</title>
<link rel="stylesheet" href="https://fonts.googleapis.com/css2?family=Roboto:wght@300;400;500;700&display=swap">
<style>
:root{
  --green:#7ac318;
  --navy:#2f3547;
  --navy-dark:#262b3a;
  --text:#333842;
  --muted:#6b707a;
  --line:#dfe3e8;
  --main-bg:#eef1f5;
  --side-bg:#f6f8fa;
  --white:#ffffff;
  --star:#f5a000;
  --purple:#a530c8;
  --orange:#f89a34;
  --bar-green:#18c134;
  --red:#e3262d;
  --page:#dde2e8;
}
*{box-sizing:border-box;margin:0;padding:0}
html,body{width:1200px;height:857px;overflow:hidden;background:var(--page);font-family:'Roboto',sans-serif;color:var(--text)}
.dashboard{position:absolute;left:0;top:34px;width:1173px;height:770px;transform:scale(1.0230);transform-origin:0 0;background:var(--main-bg);box-shadow:0 4px 20px rgba(0,0,0,.15);overflow:hidden}
.abs{position:absolute}
/* top bar */
.topbar{left:0;top:0;width:1173px;height:57px;background:var(--white);border-bottom:1px solid var(--line)}
.brand{left:0;top:0;width:223px;height:57px;background:var(--navy);display:flex;align-items:center;justify-content:center;gap:10px}
.brand-dot{width:24px;height:24px;border-radius:50%;background:var(--green)}
.brand-name{color:var(--white);font-size:17px;font-weight:400;letter-spacing:.5px}
.nav-item{top:0;height:57px;display:flex;align-items:center;justify-content:center;gap:12px;font-size:14px;color:var(--text);border-right:1px solid var(--line)}
.user{left:987px;top:0;width:186px;height:57px;border-left:1px solid var(--line);display:flex;align-items:center;padding-left:17px;gap:8px;font-size:14px;font-weight:500}
.avatar{border-radius:50%;background:linear-gradient(135deg,#7a4a34,#c89070)}
/* sub bar */
.subbar{left:0;top:57px;width:1173px;height:48px;background:var(--white);border-bottom:1px solid var(--line)}
.latest{left:0;top:0;width:223px;height:48px;background:var(--green);color:var(--white);display:flex;align-items:center;padding-left:44px;gap:12px;font-size:15px;font-weight:500}
.saved{left:223px;top:0;width:129px;height:48px;display:flex;align-items:center;padding-left:14px;font-size:14px;border-right:1px solid var(--line)}
.badge{position:absolute;left:99px;top:6px;width:13px;height:13px;border-radius:50%;background:var(--red);color:var(--white);font-size:8px;display:flex;align-items:center;justify-content:center}
.search{left:352px;top:0;width:489px;height:48px;display:flex;align-items:center;padding-left:16px;font-size:12px;color:var(--muted);border-right:1px solid var(--line)}
.drop{top:0;height:48px;display:flex;align-items:center;justify-content:center;gap:14px;font-size:13px;border-right:1px solid var(--line)}
.plus{left:1101px;top:0;width:46px;height:48px;background:var(--green);display:flex;align-items:center;justify-content:center}
/* sections */
.sidebar{left:875px;top:105px;width:298px;height:665px;background:var(--side-bg);border-left:1px solid var(--line)}
.section-title{font-size:18px;font-weight:400;color:var(--text)}
.card{top:176px;width:191px;height:227px;background:var(--white);box-shadow:0 1px 2px rgba(0,0,0,.08)}
.card-icon{position:absolute;left:78px;top:14px;width:36px;height:40px;border-radius:6px;background:#8e939c}
.card-rule{position:absolute;left:4px;right:4px;top:83px;border-top:1px solid var(--line)}
.card-label{position:absolute;left:54px;width:83px;top:71px;height:24px;border:1px solid #c8ccd2;border-radius:12px;background:var(--white);font-size:13px;display:flex;align-items:center;justify-content:center}
.card-text{position:absolute;left:0;right:0;top:108px;text-align:center;font-size:11px;line-height:16px;color:var(--muted)}
.read-more{position:absolute;left:64px;top:152px;width:64px;height:20px;border:1px solid #c8ccd2;border-radius:2px;font-size:10px;color:var(--muted);display:flex;align-items:center;justify-content:center}
.read-more.plain{border-color:transparent}
.card-foot{position:absolute;left:0;right:0;bottom:0;height:34px;border-top:1px solid var(--line);display:flex;align-items:center;padding:0 9px 0 9px;font-size:8.5px;color:var(--muted)}
.stars{color:var(--star);font-size:13px;letter-spacing:-1px;flex:1}
.meetings{left:44px;top:487px;width:790px;height:228px;background:var(--white);box-shadow:0 1px 2px rgba(0,0,0,.08)}
.meeting{top:0;width:395px;height:228px}
.meeting-photo{position:absolute;left:24px;top:34px;width:110px;height:110px;border-radius:50%}
.meeting-title{position:absolute;left:154px;top:36px;font-size:16px;font-weight:500}
.meeting-text{position:absolute;left:154px;top:62px;font-size:12.5px;line-height:18px;color:var(--muted);font-weight:300;white-space:nowrap}
.btn{position:absolute;top:130px;height:26px;width:74px;color:var(--white);font-size:12.5px;display:flex;align-items:center;justify-content:center}
.btn-green{left:154px;background:var(--green)}
.btn-navy{left:236px;background:var(--navy)}
.meeting-rule{position:absolute;left:24px;width:328px;top:177px;border-top:1px solid var(--line)}
.meeting-meta{position:absolute;left:26px;top:193px;display:flex;align-items:center;font-size:11px;color:var(--text);gap:5px;white-space:nowrap}
.meeting-meta .gap{width:16px}
/* sidebar */
.tabs{left:32px;top:37px;width:231px;height:43px}
.tab-active{position:absolute;left:0;top:0;width:125px;height:43px;border:1px solid #c8ccd2;border-bottom:none;background:var(--side-bg);display:flex;align-items:center;justify-content:center;font-size:17px}
.tab{position:absolute;left:134px;top:0;height:37px;display:flex;align-items:center;font-size:17px;white-space:nowrap}
.tabs-rule{position:absolute;left:0;width:231px;top:42px;border-top:1px solid #c8ccd2}
.tab-active-mask{position:absolute;left:1px;width:123px;top:42px;border-top:1px solid var(--side-bg)}
.reminder{left:32px;width:231px;height:81px;border-bottom:1px solid var(--line)}
.reminder .avatar{position:absolute;left:0;top:16px;width:34px;height:34px}
.reminder-text{position:absolute;left:45px;top:18px;font-size:11.5px;line-height:15px;color:var(--text);white-space:nowrap}
.reminder-date{position:absolute;left:45px;top:56px;font-size:11px;display:flex;align-items:center;gap:4px;color:var(--text)}
.calendar-btn{left:32px;top:337px;width:102px;height:29px;background:var(--green);color:var(--white);font-size:11.5px;font-weight:500;display:flex;align-items:center;justify-content:center;gap:7px}
.datarooms{left:32px;top:388px;width:229px;height:245px;background:var(--white);border:1px solid var(--line)}
.datarooms-head{height:47px;background:var(--navy);color:var(--white);font-size:16px;display:flex;align-items:center;padding-left:17px}
</style>
</head>
<body>
<main class="dashboard">

  <header class="abs topbar">
    <div class="abs brand"><span class="brand-dot"></span><span class="brand-name">PactBloom</span></div>
    <div class="abs nav-item" style="left:223px;width:114px">
      <svg width="22" height="22" viewBox="0 0 22 22"><circle cx="11" cy="11" r="8" fill="none" stroke="#333842" stroke-width="2.2" stroke-dasharray="3 2"/><circle cx="11" cy="11" r="4" fill="none" stroke="#333842" stroke-width="2"/></svg>Settings</div>
    <div class="abs nav-item" style="left:337px;width:114px">
      <svg width="22" height="20" viewBox="0 0 22 20"><path d="M2 11v7h18v-7" fill="none" stroke="#333842" stroke-width="2"/><path d="M11 2v10M7 8l4 4 4-4" fill="none" stroke="#333842" stroke-width="2"/></svg>Inbox</div>
    <div class="abs nav-item" style="left:451px;width:118px">
      <svg width="22" height="18" viewBox="0 0 22 18"><g fill="#333842"><rect x="0" y="1" width="3" height="3"/><rect x="0" y="8" width="3" height="3"/><rect x="0" y="15" width="3" height="3"/><rect x="7" y="1.5" width="15" height="2"/><rect x="7" y="8.5" width="15" height="2"/><rect x="7" y="15.5" width="15" height="2"/></g></svg>Features</div>
    <div class="abs nav-item" style="left:569px;width:120px;border-right:none;justify-content:flex-start;padding-left:18px">
      <svg width="18" height="10" viewBox="0 0 18 10"><path d="M1 5h16M5 1L1 5l4 4M13 1l4 4-4 4" fill="none" stroke="#333842" stroke-width="2"/></svg>Anyway</div>
    <div class="abs user"><span class="avatar" role="img" aria-label="User profile photo" style="width:26px;height:26px;display:block"></span>PactBloom
      <svg style="margin-left:14px" width="12" height="7" viewBox="0 0 12 7"><path d="M0 0h12L6 7z" fill="#555"/></svg></div>
  </header>

  <nav class="abs subbar">
    <div class="abs latest">
      <svg width="18" height="20" viewBox="0 0 18 20"><rect x="1" y="7" width="16" height="12" rx="1" fill="#fff"/><path d="M5 7V4a4 4 0 0 1 8 0v3" fill="none" stroke="#fff" stroke-width="2"/></svg>My Latest
      <svg style="margin-left:36px" width="12" height="8" viewBox="0 0 12 8"><path d="M0 0h12L6 8z" fill="#fff"/></svg></div>
    <div class="abs saved">Saved searches<span class="badge">5</span></div>
    <div class="abs search">Search..</div>
    <div class="abs drop" style="left:841px;width:117px">Category<svg width="10" height="7" viewBox="0 0 10 7"><path d="M1 1l4 4 4-4" fill="none" stroke="#333" stroke-width="2"/></svg></div>
    <div class="abs drop" style="left:958px;width:143px;border-right:none">CONTRACTS<svg width="10" height="7" viewBox="0 0 10 7"><path d="M1 1l4 4 4-4" fill="none" stroke="#333" stroke-width="2"/></svg></div>
    <div class="abs plus"><svg width="16" height="16" viewBox="0 0 16 16"><path d="M8 1v14M1 8h14" stroke="#fff" stroke-width="3"/></svg></div>
  </nav>

  <h2 class="abs section-title" style="left:42px;top:134px">Document Categories</h2>

  <article class="abs card" style="left:42px">
    <div class="card-icon" role="img" aria-label="Contracts category icon"></div>
    <div class="card-rule"></div><div class="card-label">Contracts</div>
    <p class="card-text">Lorem ipsum dolor sit amet<br>consectetur adcing elit,</p>
    <div class="read-more">Read More</div>
    <div class="card-foot"><span class="stars">★★★★★</span>✎&nbsp;&nbsp;|&nbsp;&nbsp;&nbsp;Total 36</div>
  </article>
  <article class="abs card" style="left:242px">
    <div class="card-icon" role="img" aria-label="Finance category icon" style="background:#2f3547"></div>
    <div class="card-rule"></div><div class="card-label">Finance</div>
    <p class="card-text">Lorem ipsum dolor sit amet<br>consectetur adcing elit,</p>
    <div class="read-more">Read More</div>
    <div class="card-foot"><span class="stars">★★★★★</span>✎&nbsp;&nbsp;|&nbsp;&nbsp;&nbsp;Total 36</div>
  </article>
  <article class="abs card" style="left:442px">
    <div class="card-icon" role="img" aria-label="Admin category icon"></div>
    <div class="card-rule"></div><div class="card-label">Admin</div>
    <p class="card-text">Lorem ipsum dolor sit amet<br>consectetur adcing elit,</p>
    <div class="read-more plain">Read More</div>
    <div class="card-foot"><span class="stars">★★★★★</span>✎&nbsp;&nbsp;|&nbsp;&nbsp;&nbsp;Total 36</div>
  </article>
  <article class="abs card" style="left:643px">
    <div class="card-icon" role="img" aria-label="HR category icon"></div>
    <div class="card-rule"></div><div class="card-label">HR</div>
    <p class="card-text">Lorem ipsum dolor sit amet<br>consectetur adcing elit,</p>
    <div class="read-more">Read More</div>
    <div class="card-foot"><span class="stars">★★★★★</span>✎&nbsp;&nbsp;|&nbsp;&nbsp;&nbsp;Total 36</div>
  </article>

  <h2 class="abs section-title" style="left:48px;top:444px">Upcoming Meetings</h2>

  <section class="abs meetings">
    <div class="abs meeting" style="left:0;border-right:1px solid var(--line)">
      <div class="meeting-photo" role="img" aria-label="Portrait of the meeting host" style="background:radial-gradient(circle at 50% 40%,#d9b49a,#5a6b80)"></div>
      <h3 class="meeting-title">Board Meetings</h3>
      <p class="meeting-text">Lorem Ipsum is simply dummy text<br>of the prining and typesetting indus-<br>try. Lorem &nbsp;Ipsum is simply.</p>
      <div class="btn btn-green">See All</div><div class="btn btn-navy">ADD</div>
      <div class="meeting-rule"></div>
      <div class="meeting-meta">
        <svg width="11" height="11" viewBox="0 0 11 11"><rect x=".5" y="1.5" width="10" height="9" fill="none" stroke="#555"/><path d="M.5 4h10" stroke="#555"/></svg>17 Jun 2016<span class="gap"></span>
        <svg width="13" height="13" viewBox="0 0 13 13"><circle cx="6.5" cy="6.5" r="5.5" fill="none" stroke="#555" stroke-width="1.4"/><path d="M6.5 3.5v3h2.5" fill="none" stroke="#555" stroke-width="1.4"/></svg>&nbsp;3:20pm<span class="gap"></span>
        <svg width="9" height="13" viewBox="0 0 9 13"><path d="M4.5 12S1 7 1 4.5a3.5 3.5 0 0 1 7 0C8 7 4.5 12 4.5 12z" fill="none" stroke="#555" stroke-width="1.4"/></svg>Harbor Road 2-4(Northwind.)
      </div>
    </div>
    <div class="abs meeting" style="left:395px">
      <div class="meeting-photo" role="img" aria-label="Portrait of the meeting host" style="left:38px;background:radial-gradient(circle at 50% 40%,#c99a80,#6a5550)"></div>
      <h3 class="meeting-title" style="left:167px">Board Meetings</h3>
      <p class="meeting-text" style="left:167px">Lorem Ipsum is simply dummy text<br>of the prining and typesetting indus-<br>try. Lorem &nbsp;Ipsum is simply.</p>
      <div class="btn btn-green" style="left:167px">See All</div><div class="btn btn-navy" style="left:249px">ADD</div>
      <div class="meeting-rule" style="left:37px"></div>
      <div class="meeting-meta" style="left:39px">
        <svg width="11" height="11" viewBox="0 0 11 11"><rect x=".5" y="1.5" width="10" height="9" fill="none" stroke="#555"/><path d="M.5 4h10" stroke="#555"/></svg>16 Agu 2016<span class="gap"></span>
        <svg width="13" height="13" viewBox="0 0 13 13"><circle cx="6.5" cy="6.5" r="5.5" fill="none" stroke="#555" stroke-width="1.4"/><path d="M6.5 3.5v3h2.5" fill="none" stroke="#555" stroke-width="1.4"/></svg>&nbsp;3:20pm<span class="gap"></span>
        <svg width="9" height="13" viewBox="0 0 9 13"><path d="M4.5 12S1 7 1 4.5a3.5 3.5 0 0 1 7 0C8 7 4.5 12 4.5 12z" fill="none" stroke="#555" stroke-width="1.4"/></svg>Harbor Road 2-4(Northwind.)
      </div>
    </div>
  </section>

  <aside class="abs sidebar">
    <div class="abs tabs">
      <div class="tabs-rule"></div>
      <div class="tab-active">Remindres</div><div class="tab-active-mask"></div>
      <div class="tab">Activty Feed</div>
    </div>

    <div class="abs reminder" style="top:80px">
      <span class="avatar" role="img" aria-label="Contact photo"></span>
      <p class="reminder-text">Price evaluation point:- Mareting<br>Co-operation Agreement Nova Ads Ltd</p>
      <p class="reminder-date"><svg width="10" height="10" viewBox="0 0 10 10"><rect x=".5" y="1" width="9" height="8.5" fill="none" stroke="#555"/><path d="M.5 3.5h9" stroke="#555"/></svg>29-6-2016</p>
    </div>
    <div class="abs reminder" style="top:161px">
      <span class="avatar" role="img" aria-label="Contact photo" style="left:4px"></span>
      <p class="reminder-text" style="left:49px">Expiring:- Security services for<br>Lakeside Rock event 2016</p>
      <p class="reminder-date" style="left:49px"><svg width="10" height="10" viewBox="0 0 10 10"><rect x=".5" y="1" width="9" height="8.5" fill="none" stroke="#555"/><path d="M.5 3.5h9" stroke="#555"/></svg>1-7-2016</p>
    </div>
    <div class="abs reminder" style="top:242px">
      <span class="avatar" role="img" aria-label="Contact photo"></span>
      <p class="reminder-text">Expiring:-Cleaning Services<br>Areement 2015</p>
      <p class="reminder-date"><svg width="10" height="10" viewBox="0 0 10 10"><rect x=".5" y="1" width="9" height="8.5" fill="none" stroke="#555"/><path d="M.5 3.5h9" stroke="#555"/></svg>6-7-2016</p>
    </div>

    <div class="abs calendar-btn"><svg width="12" height="12" viewBox="0 0 12 12"><rect x=".5" y="1.5" width="11" height="10" fill="none" stroke="#fff"/><path d="M.5 4.5h11" stroke="#fff"/></svg>CAlENDAR</div>

    <section class="abs datarooms">
      <div class="datarooms-head">Virtual Datarooms</div>
      <svg width="227" height="196" viewBox="0 0 227 196" font-family="Roboto, sans-serif" font-size="7" fill="#8a8f98">
        <circle cx="49" cy="19" r="3" fill="var(--bar-green)"/><text x="55" y="22">Seeker</text>
        <circle cx="101" cy="19" r="3" fill="var(--orange)"/><text x="107" y="22">Finder</text>
        <circle cx="146" cy="19" r="3" fill="var(--purple)"/><text x="152" y="22">Locator</text>
        <g text-anchor="end">
          <text x="34" y="53">500</text><text x="34" y="75">400</text><text x="34" y="97">300</text>
          <text x="34" y="119">200</text><text x="34" y="141">100</text><text x="34" y="163">0</text>
        </g>
        <g>
          <rect x="46" y="80" width="15" height="48" fill="var(--bar-green)"/><rect x="46" y="128" width="15" height="11" fill="var(--orange)"/><rect x="46" y="139" width="15" height="22" fill="var(--purple)"/>
          <rect x="70" y="66" width="15" height="33" fill="var(--bar-green)"/><rect x="70" y="99" width="15" height="25" fill="var(--orange)"/><rect x="70" y="124" width="15" height="37" fill="var(--purple)"/>
          <rect x="94" y="93" width="15" height="31" fill="var(--bar-green)"/><rect x="94" y="124" width="15" height="13" fill="var(--orange)"/><rect x="94" y="137" width="15" height="24" fill="var(--purple)"/>
          <rect x="118" y="99" width="15" height="13" fill="var(--bar-green)"/><rect x="118" y="112" width="15" height="18" fill="var(--orange)"/><rect x="118" y="130" width="15" height="31" fill="var(--purple)"/>
          <rect x="142" y="55" width="15" height="36" fill="var(--bar-green)"/><rect x="142" y="91" width="15" height="26" fill="var(--orange)"/><rect x="142" y="117" width="15" height="44" fill="var(--purple)"/>
          <rect x="166" y="80" width="15" height="37" fill="var(--bar-green)"/><rect x="166" y="117" width="15" height="13" fill="var(--orange)"/><rect x="166" y="130" width="15" height="31" fill="var(--purple)"/>
          <rect x="190" y="66" width="15" height="31" fill="var(--bar-green)"/><rect x="190" y="97" width="15" height="27" fill="var(--orange)"/><rect x="190" y="124" width="15" height="37" fill="var(--purple)"/>
        </g>
        <g text-anchor="middle">
          <text x="53" y="179">Mon</text><text x="77" y="179">Tue</text><text x="101" y="179">Wed</text><text x="125" y="179">Thu</text>
          <text x="149" y="179">Fri</text><text x="173" y="179">Sat</text><text x="197" y="179">Sun</text>
        </g>
      </svg>
    </section>
  </aside>

</main>
</body>
</html>
```